Halvorn - Refresh the look and feel of an existing website

We currently have an existing website www.halvornworldadvisory.example however it needs a more refreshed 'look and feel'. We are a professional consultancy that works with large corporate organisations and government. Our 'tag line' is A New Way of Thinking. We want the site to communicate "Innovation" and Leading Edge Thinking.

Target Market(s)

Corporate and Professional Clients - Organisation and Business Change

Industry/Entity Type

Management Consulting

Number of Pages Required

1 page

Font styles to use
Sans Serif

Requirements
Must have
• Must have a professional Corporate look and feel. Header 'imagery' is ok but boxes on front page need changing ... along with the words. The focus on home page needs to 'call out' 3 main consulting areas:-
• - Change & Transformation Specialists
• - Innovative Solutions
• - Digital Transformation
• Tag Line for business is ... A New Way of Thinking (Highlighting Halvorn as 'Thought Leaders' in business)
Nice to have
• Less "words' more imagery. Possibly an area for a 'video' or recent articles/blogs on the front page. Needs to have more of an 'interactive' feel. We are open to suggestions.
Should not have
• NA

```html
<!DOCTYPE html>
<html lang="en">
<head>
<meta charset="utf-8">
<title>Halvorn World Advisory</title>
<link href="https://fonts.googleapis.com/css2?family=Open+Sans:wght@300;400;600&display=swap" rel="stylesheet">
<style>
:root{
  --blue:#1a7fe6;
  --blue-deep:#0f63c9;
  --ink:#333;
  --muted:#666;
  --light:#ebebeb;
  --white:#fff;
  --black:#000;
  --line:#d9d9d9;
}
*{margin:0;padding:0;box-sizing:border-box}
html,body{width:1200px;height:2390px;overflow:hidden}
body{font-family:'Open Sans',Arial,sans-serif;color:var(--ink);background:var(--white);position:relative}
.wrap{position:absolute;left:0;width:1200px}
/* Header + hero */
.hero{top:0;height:373px;background:linear-gradient(135deg,#3a3a3a 0%,#5a5652 40%,#2f2d2b 70%,#4a3f3a 100%)}
.hero-shade{position:absolute;inset:0;background:rgba(0,0,0,.35)}
.topbar{position:absolute;left:0;top:0;width:1200px;height:51px;background:rgba(0,0,0,.45)}
.brand{position:absolute;left:210px;top:10px;display:flex;align-items:center;gap:8px;color:var(--white)}
.brand-mark{width:30px;height:30px;border:2px solid var(--white);border-radius:50%}
.brand-name{font-size:15px;font-weight:600;letter-spacing:.5px;line-height:1}
.brand-sub{font-size:7px;letter-spacing:.4px;display:block;margin-top:2px;font-weight:400}
.nav{position:absolute;right:210px;top:19px;display:flex;gap:14px;font-size:10.5px;text-transform:uppercase;color:var(--white)}
.nav .active{position:relative}
.nav .active::after{content:"";position:absolute;left:4px;right:4px;top:17px;height:2px;background:var(--blue)}
.hero-copy{position:absolute;top:144px;width:1200px;text-align:center;color:var(--white)}
.hero-copy h1{font-weight:400;font-size:23px;letter-spacing:.3px}
.hero-copy p{font-size:14px;margin-top:2px}
.hero-rule{width:48px;height:2px;background:var(--blue);margin:30px auto 0}
.btn-ghost{display:inline-block;margin-top:26px;width:112px;height:35px;line-height:33px;border:1px solid var(--white);font-size:12px;text-transform:uppercase;color:var(--white)}
.hero-arrow{position:absolute;top:181px}
/* Tagline */
.tagline{top:373px;height:107px;background:var(--light);text-align:center}
.tagline h2{font-weight:300;color:var(--blue);font-size:44px;line-height:107px;letter-spacing:.5px}
/* Feature rows */
.row{height:325px}
.half{position:absolute;top:0;width:600px;height:325px}
.half.left{left:0}.half.right{left:600px}
.photo-title{position:absolute;color:var(--white);font-weight:300;font-size:22px;line-height:32px;text-transform:uppercase}
.card{position:absolute;left:33px;width:357px;border-top:1px solid var(--line);border-left:1px solid var(--line);padding:10px 0 12px 10px}
.card h3{color:var(--blue);font-weight:400;font-size:14px;line-height:19px}
.card p{font-size:9.5px;line-height:16px;color:var(--muted);margin-top:12px}
.btn-outline{position:absolute;height:30px;line-height:28px;padding:0 9px;border:2px solid var(--blue);color:var(--blue-deep);font-size:11px;text-transform:uppercase;background:var(--white)}
.btn-outline::after{content:"";position:absolute;right:-2px;bottom:-2px;border-left:6px solid transparent;border-bottom:6px solid var(--blue)}
.solutions{position:absolute;left:209px;top:56px;width:357px;height:164px;border:1px solid var(--line);border-left:none;border-bottom:none}
.sol{position:absolute;width:110px;text-align:center;font-size:8.5px;line-height:12px;text-transform:uppercase;color:var(--ink)}
.sol svg{display:block;margin:0 auto 4px}
/* Team */
.team{top:1455px;height:320px;background:var(--light)}
.section-title{position:absolute;width:1200px;text-align:center;font-weight:300;font-size:19px;text-transform:uppercase;color:var(--ink)}
.section-rule{position:absolute;left:576px;width:48px;height:2px;background:var(--blue)}
.member{position:absolute;top:88px;width:381px;height:144px;background:var(--white)}
.member-photo{position:absolute;left:0;top:0;width:136px;height:144px;background:linear-gradient(180deg,#9cc0dc 0%,#c8d6e0 45%,#3a3a44 100%)}
.member-body{position:absolute;left:156px;top:16px;right:14px}
.member-body h4{color:var(--blue);font-weight:400;font-size:12px;text-transform:uppercase}
.member-role{font-size:9px;color:var(--ink);margin-top:1px}
.member-body p{font-size:8.5px;line-height:14px;color:var(--ink);margin-top:10px}
.member-link{position:absolute;right:14px;bottom:12px;font-size:9px;color:var(--blue);text-transform:uppercase}
.pager{position:absolute;left:580px;display:flex;gap:2px}
.pager span{width:19px;height:19px;background:var(--blue);display:flex;align-items:center;justify-content:center}
/* Clients */
.clients{top:1775px;height:240px;background:var(--white)}
.logos{position:absolute;left:210px;top:95px;display:flex;gap:20px}
.logo-box{width:113px;height:59px;border:1px solid var(--line);display:flex;align-items:center;justify-content:center;gap:6px;font-size:15px;font-weight:600;color:var(--blue-deep)}
.logo-box i{width:10px;height:10px;background:var(--blue-deep);display:block}
/* Newsletter */
.newsletter{top:2015px;height:109px;background:linear-gradient(100deg,#1f7fe0 0%,#2a8df0 45%,#1669d3 100%)}
.newsletter h3{position:absolute;left:209px;top:38px;color:var(--white);font-weight:300;font-size:25px;text-transform:uppercase}
.field{position:absolute;left:540px;top:39px;width:418px;height:29px;background:var(--white);font-size:11.5px;line-height:29px;padding-left:8px;color:#555;text-transform:uppercase}
.field-btn{position:absolute;left:958px;top:39px;width:32px;height:29px;background:#222;display:flex;align-items:center;justify-content:center}
/* Footer */
.footer{top:2124px;height:266px;background:var(--black);color:var(--white)}
.footer-brand{position:absolute;left:210px;top:42px}
.footer-about{position:absolute;left:210px;top:86px;width:250px;font-size:9px;line-height:12.5px}
.fcol{position:absolute;top:40px}
.fcol h5{font-size:12px;font-weight:600;text-transform:uppercase}
.fcol .rule{width:18px;height:2px;background:var(--blue);margin:6px 0 8px}
.fcol li{list-style:none;font-size:9px;line-height:14px}
.fcol li::before{content:"› ";color:var(--blue)}
.contact li::before{content:none}
.contact li{display:flex;gap:10px;margin-bottom:10px;line-height:12px}
.social{display:flex;gap:5px;margin-top:4px}
.social span{width:16px;height:16px;border-radius:50%;background:var(--blue)}
.copyright{position:absolute;left:210px;top:220px;width:780px;border-top:1px solid #333;text-align:center;font-size:9px;padding-top:17px}
</style>
</head>
<body>

<section class="wrap hero">
  <div role="img" aria-label="Desk scene with hands sketching plans beside a phone, mouse and coloured pens" style="position:absolute;inset:0"></div>
  <div class="hero-shade"></div>
  <header class="topbar">
    <div class="brand">
      <span class="brand-mark"></span>
      <div><span class="brand-name">HALVORN</span><span class="brand-sub">WORLD ADVISORY</span></div>
    </div>
    <nav class="nav">
      <span class="active">Home</span><span>About Us</span><span>Our Services</span><span>Solutions</span><span>What's Happening</span><span>Contact Us</span>
    </nav>
  </header>
  <svg class="hero-arrow" style="left:153px" width="38" height="20" viewBox="0 0 38 20"><path d="M37 10H2M10 2 2 10l8 8" fill="none" stroke="#fff" stroke-width="2"/></svg>
  <svg class="hero-arrow" style="left:1010px" width="38" height="20" viewBox="0 0 38 20"><path d="M1 10h35M28 2l8 8-8 8" fill="none" stroke="#fff" stroke-width="2"/></svg>
  <div class="hero-copy">
    <h1>WE BRING A DYNAMIC AND LEADING EDGE APPROACH</h1>
    <p>To understand your business challenge and develop the optimum solution.</p>
    <div class="hero-rule"></div>
    <span class="btn-ghost">Learn More</span>
  </div>
</section>

<section class="wrap tagline"><h2>A NEW WAY OF THINKING</h2></section>

<section class="wrap row" style="top:480px">
  <div class="half left" role="img" aria-label="Desk with coffee pot, cup, tablet and notebook" style="background:linear-gradient(135deg,#6b6b6b 0%,#3d3d3d 50%,#222 100%)">
    <div class="photo-title" style="right:34px;top:130px;text-align:right">Change &amp;<br>Transformation Specialists</div>
  </div>
  <div class="half right">
    <div class="card" style="top:64px">
      <h3>We partner with our clients to develop strategies, plans and programs to support change of all types.</h3>
      <p>We partner with our clients to develop programs that will support all aspects of organisational transformation. From strategy and design through to implementation, we can support at all levels of transformation. All our methods and models have been utilised successfully across multiple organisations, delivering strong and sustainable results.</p>
    </div>
    <span class="btn-outline" style="left:33px;top:231px">Read More</span>
  </div>
</section>

<section class="wrap row" style="top:805px">
  <div class="half left">
    <div class="solutions">
      <div class="sol" style="left:-6px;top:20px">
        <svg width="26" height="22" viewBox="0 0 26 22"><g fill="#1a7fe6"><circle cx="13" cy="4" r="3.5"/><rect x="8" y="8" width="10" height="6" rx="2"/><circle cx="5" cy="12" r="3"/><circle cx="21" cy="12" r="3"/><rect x="1" y="15" width="8" height="6" rx="2"/><rect x="17" y="15" width="8" height="6" rx="2"/></g></svg>
        Community<br>Solutions</div>
      <div class="sol" style="left:114px;top:20px">
        <svg width="26" height="22" viewBox="0 0 26 22"><rect x="1" y="5" width="24" height="16" rx="2" fill="#1a7fe6"/><path d="M9 5V2h8v3" fill="none" stroke="#1a7fe6" stroke-width="2"/><rect x="11" y="11" width="4" height="3" fill="#fff"/></svg>
        Business<br>Solutions</div>
      <div class="sol" style="left:234px;top:20px">
        <svg width="26" height="24" viewBox="0 0 26 24"><path d="M13 1v22M13 1l-4 4M13 1l4 4M13 12l-8 6M13 12l8-6M5 18v-4M5 18h4M21 6h-4M21 6v4" fill="none" stroke="#1a7fe6" stroke-width="2.5"/></svg>
        Our<br>Approach</div>
      <div class="sol" style="left:54px;top:92px">
        <svg width="26" height="22" viewBox="0 0 26 22"><path d="M4 20C6 10 12 4 22 2c-2 8-8 14-18 18z" fill="#1a7fe6"/><path d="M2 21h22" stroke="#1a7fe6" stroke-width="2"/></svg>
        Environmental<br>Solutions</div>
      <div class="sol" style="left:174px;top:92px">
        <svg width="26" height="24" viewBox="0 0 26 24"><circle cx="13" cy="10" r="8" fill="none" stroke="#1a7fe6" stroke-width="2.5"/><circle cx="13" cy="10" r="4" fill="#1a7fe6"/><path d="M13 18v4M8 23h10" stroke="#1a7fe6" stroke-width="2"/></svg>
        Global<br>Solutions</div>
    </div>
    <span class="btn-outline" style="left:422px;top:239px">View All Solutions</span>
  </div>
  <div class="half right" role="img" aria-label="Hands holding a sheet sketched with innovation diagrams" style="background:radial-gradient(ellipse at 60% 45%,#e4e2dc 0%,#cfcbc2 35%,#2a2a2a 60%,#111 100%)">
    <div class="photo-title" style="left:33px;top:130px">Innovative<br>Solutions</div>
  </div>
</section>

<section class="wrap row" style="top:1130px">
  <div class="half left" role="img" aria-label="Two head silhouettes overlaid with glowing circuit lines" style="background:linear-gradient(120deg,#0b0b12 0%,#2b2550 35%,#1a1630 55%,#3a3560 70%,#0a0a10 100%)">
    <div class="photo-title" style="right:34px;top:130px;text-align:right">Digital<br>Transformation</div>
  </div>
  <div class="half right">
    <div class="card" style="top:58px">
      <h3>Lorem Ipsum is simply dummy text</h3>
      <p>Lorem Ipsum is simply dummy text of the printing and typesetting industry. Lorem Ipsum has been the industry's standard dummy text ever since the 1500s, when an unknown printer took a galley of type and scrambled it to make a type specimen book. Lorem Ipsum is simply dummy text of the printing and typesetting industry. Lorem Ipsum has been the industry's standard dummy text ever since the 1500s, when an unknown printer took a galley of type and scrambled it to make a type specimen book.</p>
    </div>
    <span class="btn-outline" style="left:33px;top:238px">Read More</span>
  </div>
</section>

<section class="wrap team">
  <h3 class="section-title" style="top:27px">Our Team</h3>
  <div class="section-rule" style="top:62px"></div>
  <article class="member" style="left:210px">
    <div class="member-photo" role="img" aria-label="Portrait photo of Maren Ostby"></div>
    <div class="member-body">
      <h4>Maren Ostby</h4>
      <div class="member-role">Founder &amp; Managing Director</div>
      <p>Maren specialises in Strategy Development, Transformation, Solution Development, Organisational Change, Program Governance, Process Efficiencies, Mergers and Acquisitions, New Business Set-up</p>
    </div>
    <span class="member-link">Full Profile →</span>
  </article>
  <article class="member" style="left:609px">
    <div class="member-photo" role="img" aria-label="Portrait photo of Elise Tanner"></div>
    <div class="member-body">
      <h4>Elise Tanner</h4>
      <div class="member-role">Managing Director Asia Pacific</div>
      <p>Elise specialises in Organisational Transformation, Cultural Change, Strategic Planning, Leadership Development, Change Management, Team Building, Executive Coaching, and Mediation</p>
    </div>
    <span class="member-link">Full Profile →</span>
  </article>
  <div class="pager" style="top:259px">
    <span><svg width="8" height="10" viewBox="0 0 8 10"><path d="M6 1 2 5l4 4" fill="none" stroke="#fff" stroke-width="1.6"/></svg></span>
    <span><svg width="8" height="10" viewBox="0 0 8 10"><path d="M2 1l4 4-4 4" fill="none" stroke="#fff" stroke-width="1.6"/></svg></span>
  </div>
</section>

<section class="wrap clients">
  <h3 class="section-title" style="top:32px">Our Clients</h3>
  <div class="section-rule" style="top:67px"></div>
  <div class="logos">
    <div class="logo-box">Kestrel</div>
    <div class="logo-box"><i></i>Oakvale</div>
    <div class="logo-box">Civic Desk</div>
    <div class="logo-box">State Works</div>
    <div class="logo-box">Careline</div>
    <div class="logo-box">Veronta</div>
  </div>
  <div class="pager" style="top:180px">
    <span><svg width="8" height="10" viewBox="0 0 8 10"><path d="M6 1 2 5l4 4" fill="none" stroke="#fff" stroke-width="1.6"/></svg></span>
    <span><svg width="8" height="10" viewBox="0 0 8 10"><path d="M2 1l4 4-4 4" fill="none" stroke="#fff" stroke-width="1.6"/></svg></span>
  </div>
</section>

<section class="wrap newsletter">
  <h3>Subscribe Newsletter</h3>
  <div class="field">Enter your email address</div>
  <div class="field-btn"><svg width="14" height="10" viewBox="0 0 14 10"><path d="M0 5h12M8 1l4 4-4 4" fill="none" stroke="#fff" stroke-width="1.6"/></svg></div>
</section>

<footer class="wrap footer">
  <div class="brand footer-brand" style="top:42px">
    <span class="brand-mark"></span>
    <div><span class="brand-name">HALVORN</span><span class="brand-sub">WORLD ADVISORY</span></div>
  </div>
  <p class="footer-about">The team at Halvorn World Advisory has wide ranging experience and is well-placed to advise your business on transformational change, problem resolution, strategy development and implementation, business planning and investment propositions, all aspects of human resource management and executive leadership development.</p>
  <div class="fcol" style="left:477px">
    <h5>About Us</h5><div class="rule"></div>
    <ul><li>Our Team</li><li>Our Values</li><li>Our Clients</li><li>Giving Back</li></ul>
  </div>
  <div class="fcol" style="left:610px;width:120px">
    <h5>Our Services</h5><div class="rule"></div>
    <ul><li>Strategy and Design</li><li>Transformation</li><li>Change &amp; Culture</li><li>Organisational Development</li><li>Project Management</li><li>Organisational Efficiency</li><li>Specialist Placements</li></ul>
  </div>
  <div class="fcol contact" style="left:743px;width:230px">
    <h5>Get In Touch</h5><div class="rule"></div>
    <ul>
      <li><svg width="8" height="11" viewBox="0 0 8 11"><path d="M4 11C1 7 0 5 0 4a4 4 0 0 1 8 0c0 1-1 3-4 7z" fill="#1a7fe6"/><circle cx="4" cy="4" r="1.5" fill="#000"/></svg><span style="font-size:9px">PO Box 14 Harbour Lane West Eastvale 4100<br>AUSTRALIA In Australia: 1300 555 010</span></li>
      <li><svg width="9" height="9" viewBox="0 0 9 9"><path d="M1 0h2l1 2-1 1a5 5 0 0 0 3 3l1-1 2 1v2c-5 0-9-4-9-8z" fill="#1a7fe6"/></svg><span style="font-size:9px">(+610) 5550 1234</span></li>
      <li><svg width="10" height="8" viewBox="0 0 10 8"><rect width="10" height="8" fill="#1a7fe6"/><path d="M0 0l5 4 5-4" fill="none" stroke="#000"/></svg><span style="font-size:9px">info@halvornworldadvisory.example</span></li>
    </ul>
    <div class="social"><span></span><span></span><span></span><span></span></div>
  </div>
  <div class="copyright">Copyright © 2016 Halvorn World Advisory</div>
</footer>

</body>
</html>
```